Business Card Design

We are a commercial real estate brokerage in San Francisco, leasing office buildings downtown.
I would like a clean, elegant look. Simple but powerful .

Industry/Entity Type

Business

Contact Information for Business Card

Derek Hollings
lic# 02875140
415.287.6041
derek@vexa-commercial.com
vexa-commercial.com

```html
<!DOCTYPE html>
<html lang="en">
<head>
<meta charset="utf-8">
<title>Vexa Commercial — Business Card</title>
<link rel="stylesheet" href="https://fonts.googleapis.com/css2?family=Jost:wght@500;600&family=Open+Sans:wght@400;600&display=swap">
<style>
  :root {
    --stage: #ecebe8;
    --card-dark: #0e0f11;
    --card-light: #f1f1f1;
    --slate: #7c8fad;
    --slate-deep: #5e7191;
    --graphite: #55585d;
    --ink: #2e3033;
    --ink-soft: #4a4d52;
  }
  * { box-sizing: border-box; margin: 0; padding: 0; }
  html, body { width: 1200px; height: 768px; overflow: hidden; }
  body {
    background: var(--stage);
    position: relative;
    font-family: "Open Sans", Arial, sans-serif;
  }
  .card {
    position: absolute;
    width: 520px;
    height: 298px;
    border-radius: 3px;
    overflow: hidden;
    box-shadow: 0 10px 24px rgba(0,0,0,0.18);
  }
  .card--front { left: 50px; top: 90px; background: var(--card-dark); }
  .card--back  { left: 630px; top: 380px; background: var(--card-light); }

  .wordmark {
    position: absolute;
    display: flex;
    align-items: center;
    gap: 14px;
  }
  .wordmark__mark {
    width: 22px; height: 22px;
    background: var(--slate);
  }
  .wordmark__name {
    font-family: "Jost", Arial, sans-serif;
    font-weight: 600;
    text-transform: uppercase;
    letter-spacing: 1px;
    color: var(--slate);
    line-height: 1;
    white-space: nowrap;
  }
  .card--front .wordmark { left: 110px; top: 128px; }
  .card--front .wordmark__name { font-size: 36px; }
  .card--back .wordmark { left: 110px; top: 60px; }
  .card--back .wordmark__name { font-size: 30px; }

  .holder {
    position: absolute;
    left: 34px; top: 135px;
  }
  .holder__name {
    font-family: "Jost", Arial, sans-serif;
    font-weight: 600;
    font-size: 19px;
    color: var(--ink);
  }
  .holder__role {
    font-size: 11px;
    color: var(--ink-soft);
    margin-top: 2px;
  }

  .contact {
    position: absolute;
    left: 300px; top: 176px;
    list-style: none;
    font-size: 13px;
    color: var(--ink);
    line-height: 19px;
  }
  .contact__item { display: flex; align-items: center; gap: 8px; }
  .contact__icon { width: 11px; height: 11px; fill: var(--slate-deep); flex: none; }
  .contact__licence { margin-top: 1px; }

  .card__band {
    position: absolute;
    left: 0; bottom: 0;
    width: 520px; height: 70px;
  }
</style>
</head>
<body>

  <section class="card card--front" aria-label="Card front">
    <div class="wordmark">
      <span class="wordmark__mark"></span>
      <span class="wordmark__name">Vexa Commercial</span>
    </div>
  </section>

  <section class="card card--back" aria-label="Card back">
    <div class="wordmark">
      <span class="wordmark__mark"></span>
      <span class="wordmark__name">Vexa Commercial</span>
    </div>

    <div class="holder">
      <p class="holder__name">Derek Hollings</p>
      <p class="holder__role">Managing Director</p>
    </div>

    <ul class="contact">
      <li class="contact__item">
        <svg class="contact__icon" viewBox="0 0 12 12"><path d="M2.5 0.5h2l1 3-1.5 1a7 7 0 0 0 3.5 3.5l1-1.5 3 1v2a1 1 0 0 1-1 1A10 10 0 0 1 1.5 1.5a1 1 0 0 1 1-1z"/></svg>
        415.287.6041
      </li>
      <li class="contact__item">
        <svg class="contact__icon" viewBox="0 0 12 12"><path d="M0 2h12v8H0z M0.8 2.6 6 6.6l5.2-4" fill="none" stroke="#5e7191" stroke-width="1.2"/></svg>
        derek@vexa-commercial.com
      </li>
      <li class="contact__item">
        <svg class="contact__icon" viewBox="0 0 12 12"><circle cx="6" cy="6" r="5.4"/><path d="M0.6 6h10.8M6 0.6v10.8M2 3h8M2 9h8" stroke="#f1f1f1" stroke-width="0.8" fill="none"/></svg>
        www.vexa-commercial.com
      </li>
      <li class="contact__licence">LIC# 02875140</li>
    </ul>

    <svg class="card__band" viewBox="0 0 520 70" preserveAspectRatio="none" aria-hidden="true">
      <polygon points="0,0 0,8 345,70 520,70 520,62 360,62" fill="var(--slate)"/>
      <polygon points="330,70 360,62 520,62 520,70" fill="var(--graphite)"/>
    </svg>
  </section>

</body>
</html>
```